Do i have coronavirus, flue or cold?

Using information from QRV and government agencies we want to make a easy to read infographic helping patients see if they have coronavirus, the flu or a cold. Using a flow diagram or whatever you think will make it easy to read and digest for the average lamen.

Information is in the word document and in the chart.

We are www.tovipharm.co.uk attached is our brand guidelines, we will be putting this infographic on our website and email/sms it to all of our 300,000 patients.

```html
<!DOCTYPE html>
<html lang="en">
<head>
<meta charset="utf-8">
<title>Coronavirus symptoms – Tovipharm</title>
<link href="https://fonts.googleapis.com/css2?family=Jost:wght@400;500;600&display=swap" rel="stylesheet">
<style>
  :root {
    --navy: #06033a;
    --blue: #5b8cf0;
    --royal: #2a2fa8;
    --panel: #e3eff3;
    --panel-deep: #d6e7ee;
    --rule: #3b3f6e;
    --band-light: #dfecf2;
    --white: #ffffff;
    --ink: #0c0a3a;
  }
  * { box-sizing: border-box; margin: 0; padding: 0; }
  html, body { width: 1200px; height: 2320px; overflow: hidden; background: var(--white); }
  body { font-family: "Jost", "Futura", sans-serif; color: var(--ink); position: relative; }

  .top-strip { position: absolute; left: 0; top: 0; width: 1200px; height: 26px; background: var(--band-light); }

  .page-title { position: absolute; top: 42px; width: 1200px; text-align: center; font-size: 94px; line-height: 120px; font-weight: 400; color: var(--navy); letter-spacing: 1px; }
  .page-title .accent { color: var(--blue); }

  .intro { position: absolute; top: 176px; left: 0; width: 1200px; height: 180px; background: var(--navy); color: var(--white); padding: 20px 22px 0; font-size: 26px; line-height: 34px; text-align: justify; text-align-last: center; }

  .question { position: absolute; top: 404px; width: 1200px; text-align: center; font-size: 48px; font-weight: 400; color: var(--navy); letter-spacing: 0.5px; }

  .symptom-panel { position: absolute; left: 0; width: 1200px; background: var(--panel); overflow: hidden; }
  .symptom-panel .rule { position: absolute; top: 24px; left: 16px; width: 1170px; height: 2px; background: var(--rule); }
  .symptom-panel h2 { position: absolute; left: 71px; font-size: 48px; font-weight: 600; color: var(--navy); }
  .symptom-list { position: absolute; list-style: none; font-size: 26px; line-height: 48px; color: var(--navy); }
  .symptom-list li { position: relative; }
  .symptom-list li::before { content: "·"; position: absolute; font-size: 24px; }
  .panel-flu { top: 494px; height: 582px; }
  .panel-flu h2 { top: 34px; }
  .panel-flu .symptom-list { top: 106px; left: 88px; width: 700px; }
  .panel-flu .symptom-list li::before { left: -45px; }
  .panel-cold { top: 1119px; height: 596px; }
  .panel-cold h2 { top: 62px; }
  .panel-cold .symptom-list { top: 143px; left: 77px; }
  .panel-cold .symptom-list li::before { left: -34px; }

  .illustration { position: absolute; border-radius: 50% 50% 8px 8px; }
  .illus-flu { left: 720px; top: 36px; width: 330px; height: 420px; background: linear-gradient(180deg, var(--panel-deep), #c8d7f2 60%, #3035b0 100%); }
  .illus-cold { left: 640px; top: 110px; width: 480px; height: 440px; background: linear-gradient(180deg, var(--panel-deep), #c8d7f2 55%, #2f34ae 100%); }

  .help-band { position: absolute; top: 1752px; left: 0; width: 1200px; height: 117px; background: var(--navy); color: var(--white); font-size: 53px; font-weight: 600; text-align: center; line-height: 117px; letter-spacing: 0.5px; }

  .brand-block { position: absolute; top: 1900px; left: 40px; width: 480px; text-align: center; }
  .brand-block .lead { font-size: 48px; font-weight: 600; color: var(--navy); letter-spacing: 0.5px; }
  .brand-name { display: flex; align-items: center; justify-content: center; gap: 20px; height: 170px; }
  .brand-name .dot { width: 70px; height: 70px; border-radius: 50%; background: var(--royal); }
  .brand-name span { font-size: 76px; font-weight: 600; color: var(--royal); }
  .brand-block .tagline { font-size: 31px; font-weight: 600; color: var(--navy); letter-spacing: 0.5px; }
  .brand-block .tagline .accent { color: var(--blue); }

  .delivery { position: absolute; top: 1900px; left: 602px; width: 560px; }
  .delivery h3 { font-size: 48px; font-weight: 600; line-height: 63px; color: var(--navy); }
  .delivery h3 .accent { color: var(--blue); }
  .delivery p { margin-top: 48px; font-size: 23px; line-height: 42px; color: var(--navy); }

  .footer-strip { position: absolute; top: 2245px; left: 0; width: 1200px; height: 20px; background: var(--band-light); }
  .footer { position: absolute; top: 2273px; width: 1200px; text-align: center; font-size: 25px; color: var(--navy); }
</style>
</head>
<body>
  <div class="top-strip"></div>

  <h1 class="page-title">Coronavirus <span class="accent">symptoms</span></h1>

  <p class="intro">The most common symptoms of COVID-19 are fever, tiredness, and dry cough. Some patients may have aches and pains, nasal congestion, runny nose, sore throat or diarrhoea. These symptoms are usually mild and begin gradually. Some people become infected but don’t develop any symptoms and don't feel unwell.</p>

  <p class="question">Do i have coronavirus, flue or cold?</p>

  <section class="symptom-panel panel-flu">
    <div class="rule"></div>
    <div class="illustration illus-flu" role="img" aria-label="Illustration of a person in a face mask and scarf coughing, beside a potted plant and virus particles"></div>
    <h2>Flu symptoms</h2>
    <ul class="symptom-list">
      <li>Fever or feeling feverish/chills</li>
      <li>Cough</li>
      <li>Sore throat</li>
      <li>Runny or stuffy nose</li>
      <li>Muscle or body aches</li>
      <li>Headaches</li>
      <li>Fatigue (tiredness)</li>
      <li>Some people may have vomiting and diarrhoea,<br>though this is more common in children than adults.</li>
    </ul>
  </section>

  <section class="symptom-panel panel-cold">
    <div class="rule"></div>
    <div class="illustration illus-cold" role="img" aria-label="Illustration of a person in a face mask holding their head and a thermometer, beside a potted plant and virus particles"></div>
    <h2>Cold symptoms</h2>
    <ul class="symptom-list">
      <li>a blocked or runny nose</li>
      <li>a sore throat</li>
      <li>headaches</li>
      <li>muscle aches</li>
      <li>coughs</li>
      <li>sneezing</li>
      <li>a raised temperature</li>
      <li>pressure in your ears and face</li>
      <li>loss of taste and smell</li>
    </ul>
  </section>

  <div class="help-band">Here to help you:&nbsp; 0115 496 0123</div>

  <div class="brand-block">
    <p class="lead">BECAUSE FOR</p>
    <div class="brand-name"><div class="dot"></div><span>Tovipharm</span></div>
    <p class="tagline">YOUR HEALTH <span class="accent">COMES FIRST</span></p>
  </div>

  <div class="delivery">
    <h3>Medicine delivered<br><span class="accent">discreetly</span> to your door</h3>
    <p>Get the same genuine medicines delivered<br>to your door in as little as 24 hours as you<br>would from your GP - without the wait.</p>
  </div>

  <div class="footer-strip"></div>
  <p class="footer">© Tovipharm 2020 - Company Reg. Number: 10482736</p>
</body>
</html>
```